Software company stationery project
VOLTA Systems business cards, letterhead, stationery
Software company stationery project -
Creative Brief
Professional
Marcus Hale
President
217 Orchard Lane Tuckahoe, NY 10725
(855) 294-KOVU (5688)
marcus.hale@KovuSystems.example
www.kovusystems.example
Open to 2 sided or 1, and to your recommended font. Current website is under total reconstruction but the content will be similar. Would like to see if phrase could be used on card - "evidence and property specialists". Software is for police dept's. evidence/property rooms, and tracking those items.

```html
<!DOCTYPE html>
<html lang="en">
<head>
<meta charset="utf-8">
<title>VOLTA Systems Stationery</title>
<link href="https://fonts.googleapis.com/css2?family=Roboto:wght@400;700;900&display=swap" rel="stylesheet">
<style>
  :root {
    --paper: #ffffff;
    --backdrop: #ffffff;
    --ink: #1a1a1a;
    --muted: #555555;
    --accent: #c8102e;
    --edge: #d6d6d6;
    --flap-line: #bdbdbd;
    --seal-light: #fbeef0;
    --seal-mid: #f1d3d8;
    --shadow: rgba(0,0,0,0.18);
  }
  * { margin: 0; padding: 0; box-sizing: border-box; }
  html, body {
    width: 1200px; height: 681px; overflow: hidden;
    background: var(--backdrop);
    font-family: "Roboto", Arial, sans-serif;
    color: var(--ink);
  }
  .sheet {
    position: absolute;
    background: var(--paper);
    border: 1px solid var(--edge);
    box-shadow: 2px 3px 6px var(--shadow);
  }
  .brand { display: flex; align-items: center; gap: 5px; }
  .brand-mark { background: var(--accent); flex: none; }
  .brand-name { font-weight: 900; color: var(--ink); white-space: nowrap; line-height: 1; }
  .contact-line { font-size: 7px; color: var(--muted); line-height: 1.5; white-space: nowrap; }
  .rule-pair { position: absolute; }
  .rule-pair .rule-dark { height: 3px; background: var(--ink); }
  .rule-pair .rule-red { height: 3px; background: var(--accent); margin-top: 3px; }

  /* envelope front */
  .envelope-front { left: 60px; top: 96px; width: 410px; height: 216px; }
  .envelope-front .brand { position: absolute; left: 14px; top: 14px; }
  .envelope-front .brand-mark { width: 12px; height: 12px; }
  .envelope-front .brand-name { font-size: 18px; }
  .envelope-front .contact-line { position: absolute; left: 14px; top: 38px; font-size: 6px; }
  .envelope-front .rule-pair { left: 0; right: 42px; bottom: 18px; }

  /* envelope back */
  .envelope-back { left: 60px; top: 360px; width: 410px; height: 228px; }
  .envelope-back .flap { position: absolute; left: 0; top: 0; width: 100%; height: 100%; }
  .seal-area {
    position: absolute; left: 225px; top: 31px; width: 30px; height: 34px;
    border-radius: 3px;
    background: linear-gradient(160deg, var(--seal-light), var(--seal-mid));
  }

  /* letterhead */
  .letterhead { left: 619px; top: 48px; width: 375px; height: 581px; }
  .letterhead .brand { position: absolute; left: 20px; top: 36px; }
  .letterhead .brand-mark { width: 14px; height: 14px; }
  .letterhead .brand-name { font-size: 21px; }
  .letterhead .contact-block { position: absolute; left: 20px; top: 64px; }
  .letterhead .contact-line { font-size: 6px; }
  .letterhead .rule-pair { left: 0; right: 34px; bottom: 35px; }

  /* business card */
  .business-card { left: 970px; top: 163px; width: 140px; height: 106px; }
  .business-card .brand { position: absolute; left: 9px; top: 9px; gap: 4px; }
  .business-card .brand-mark { width: 8px; height: 8px; }
  .business-card .brand-name { font-size: 12px; }
  .business-card .person { position: absolute; left: 9px; top: 36px; }
  .business-card .person-name { font-size: 7px; font-weight: 700; line-height: 1.3; }
  .business-card .person-title { font-size: 5.5px; color: var(--muted); line-height: 1.3; }
  .business-card .contact-block { position: absolute; left: 9px; bottom: 8px; }
  .business-card .contact-line { font-size: 5px; }
</style>
</head>
<body>

<section class="sheet envelope-front">
  <div class="brand"><span class="brand-mark"></span><span class="brand-name">VOLTA Systems</span></div>
  <p class="contact-line">217 Orchard Lane | Tuckahoe, NY 10725</p>
  <div class="rule-pair"><div class="rule-dark"></div><div class="rule-red"></div></div>
</section>

<section class="sheet envelope-back">
  <svg class="flap" viewBox="0 0 410 228" preserveAspectRatio="none" aria-hidden="true">
    <polyline points="0,4 24,84 386,84 410,4" fill="none" stroke="var(--flap-line)" stroke-width="1"/>
  </svg>
  <div class="seal-area" role="img" aria-label="Area for the flap seal artwork"></div>
</section>

<section class="sheet letterhead">
  <div class="brand"><span class="brand-mark"></span><span class="brand-name">VOLTA Systems</span></div>
  <div class="contact-block">
    <p class="contact-line">217 Orchard Lane | Tuckahoe, NY 10725</p>
    <p class="contact-line">Toll Free: (855) 294-KOVU (5688) | Fax: (855) 294-5689</p>
    <p class="contact-line">www.kovusystems.example</p>
  </div>
  <div class="rule-pair"><div class="rule-dark"></div><div class="rule-red"></div></div>
</section>

<section class="sheet business-card">
  <div class="brand"><span class="brand-mark"></span><span class="brand-name">VOLTA Systems</span></div>
  <div class="person">
    <p class="person-name">Marcus Hale</p>
    <p class="person-title">President</p>
  </div>
  <div class="contact-block">
    <p class="contact-line">217 Orchard Lane | Tuckahoe, NY 10725</p>
    <p class="contact-line">(855) 294-KOVU (5688)</p>
    <p class="contact-line">marcus.hale@KovuSystems.example</p>
    <p class="contact-line">www.kovusystems.example</p>
  </div>
</section>

</body>
</html>
```